Loftwise.com ;Take Yourself Up to the Next Level. More success, higher productivity, better health.

PLEASE READ IT CAREFULLY
I HAVE RECEIVED SOME FIRST DESIGNS AND I HAVE A FEELING THAT ALMOST NOBODY HAS READ THE BRIEFING CAREFULLY.

What I need actually is the design of the main visual
THE MAIN VISUAL MUST COMMUNICATE THE CONCEPT.
THIS WEBSITE IS ABOUT THE PERSONAL DEVELOPMENT.

The change of the main visual may be linked with other changes of other elements of the homepage, but this is the secondary task.

BACKGROUND
I have launched a blog on healthy productivity: loftwise.com

The problem is that the main visual does not communicate clearly what the website is about.

Currently I have a blog with advice on healthy productivity and a shop. In teh future I would like to offer stress management courses, fitness boot camps for executives, mindefulness courses, courses for healthy sleep and work-life balance.

The task is to develop the homepage which communicates the current positioning:

Loft Wise-
Take Yourself Up to the Next Level. More Success, Higher Productivity, Better Health.

The homepage should contain all the blocks of the current homepage. Actually the main task is to find the powerful design representation of the website positioning.
Updates

Low design quality

Target Market(s)

US executives, managers and entrepreneurs

Requirements
Must have
• You should keep in principle the current color code which is green, blue, grey
• The design project must contain all the current homepage elements like blog, testimonial, footnote etc

```html
<!DOCTYPE html>
<html lang="en">
<head>
<meta charset="utf-8">
<title>Loft Wise – Take Yourself Up to the Next Level</title>
<link href="https://fonts.googleapis.com/css2?family=Montserrat:wght@500;600;700;800&family=Open+Sans:wght@400;600;700&display=swap" rel="stylesheet">
<style>
:root{
  --green:#6cbf2c;
  --blue:#1aa3e6;
  --ink:#1e1e1e;
  --grey-panel:#5a5a5a;
  --soft:#f3f0f0;
  --dark:#363636;
  --footer:#2a2a2a;
  --muted:#555;
}
*{box-sizing:border-box;margin:0;padding:0}
html,body{width:1200px;height:4307px;overflow:hidden}
body{position:relative;font-family:"Open Sans",sans-serif;color:var(--ink);background:#fff}
.abs{position:absolute}
.btn{position:absolute;display:flex;align-items:center;justify-content:center;background:var(--green);color:#fff;font-family:"Montserrat",sans-serif;font-weight:700;letter-spacing:.3px}

/* header */
.site-header{position:absolute;left:0;top:0;width:1200px;height:114px;background:#fff}
.brand{position:absolute;display:flex;align-items:center;gap:10px;font-family:"Montserrat",sans-serif;font-weight:500;letter-spacing:4px}
.brand .mark{width:22px;height:22px;border-radius:50%;background:var(--green)}
.follow{left:636px;top:32px;display:flex;align-items:center;gap:6px;font-size:10px;font-weight:700;font-family:"Montserrat",sans-serif}
.follow span.dot{width:18px;height:18px;border-radius:50%;display:inline-block}
.nav{left:459px;top:80px;display:flex;gap:32px;font-family:"Montserrat",sans-serif;font-weight:600;font-size:12px}
.nav .active{color:var(--green)}

/* hero */
.hero{left:0;top:114px;width:1200px;height:540px;background:radial-gradient(circle at 30% 45%,#7a5a48 0%,#3d2a24 35%,#1d1614 70%),#1d1614}
.hero-glow{left:700px;top:114px;width:500px;height:540px;background:radial-gradient(circle at 70% 30%,rgba(255,170,60,.35),transparent 55%)}
.hero-box{left:668px;top:227px;width:478px;height:295px;background:rgba(25,22,22,.82);color:#fff;padding:28px 38px}
.hero-box h1{font-family:"Montserrat",sans-serif;font-weight:600;font-size:37px;line-height:1}
.hero-box p{font-size:24px;margin-top:16px}
.hero-box ul{list-style:none;margin-top:18px}
.hero-box li{font-family:"Montserrat",sans-serif;font-weight:800;font-size:25px;display:flex;align-items:center;gap:16px;height:41px}
.dots{left:575px;top:602px;display:flex;gap:6px}
.dots i{width:7px;height:7px;border-radius:50%;background:#fff;display:block}
.dots i.on{background:var(--green)}

/* topics */
.topics{left:0;top:654px;width:1200px;height:653px;background:var(--soft)}
.section-title{position:absolute;left:0;width:1200px;text-align:center;font-family:"Montserrat",sans-serif;font-weight:600;font-size:28px;line-height:39px}
.grid{left:30px;top:830px;width:1154px;display:grid;grid-template-columns:repeat(5,1fr);gap:9px 10px}
.card{height:210px;background:#fff;display:flex;flex-direction:column;align-items:center;justify-content:center;text-align:center;font-family:"Montserrat",sans-serif;font-weight:600;font-size:13px;line-height:20px;color:var(--ink)}
.card svg{margin-bottom:22px}
.card.hl{background:var(--blue);color:#fff}
.card.hl .more{margin-top:10px;border:1px solid #fff;font-size:10px;padding:2px 8px}
.card.all{background:var(--green);color:#fff;font-size:16px;font-weight:700}

/* welcome */
.welcome-photo{left:0;top:1307px;width:664px;height:493px;background:linear-gradient(180deg,#e9edf2 0%,#8fa0b4 40%,#2c3848 75%,#4a4640 100%)}
.welcome{left:664px;top:1307px;width:536px;height:493px;background:var(--grey-panel);color:#fff}
.welcome .intro{position:absolute;left:70px;top:66px;font-family:"Montserrat",sans-serif;font-weight:600;font-size:28px}
.welcome h2{position:absolute;left:70px;top:100px;font-family:"Montserrat",sans-serif;font-weight:800;font-size:38px}
.welcome p{position:absolute;left:70px;top:168px;width:360px;font-size:19.5px;line-height:28px}

/* testimonials */
.testimonials{left:0;top:1800px;width:1200px;height:593px;background:linear-gradient(135deg,#f4f4f4 0%,#dcdcdc 25%,#f7f7f7 50%,#d8d8d8 75%,#f2f2f2 100%)}
.quote-box{left:222px;top:1962px;width:750px;height:291px;background:#fff;border:4px solid #d5d5d5;text-align:center}
.quote-box p{position:absolute;left:150px;top:60px;width:450px;font-size:18.5px;line-height:27px;color:#333}
.qmark{position:absolute;font-family:"Montserrat",sans-serif;font-weight:800;font-size:48px;color:var(--green)}
.author{position:absolute;left:270px;top:242px;display:flex;gap:14px;align-items:center;text-align:left}
.author .avatar{width:50px;height:50px;border-radius:50%;border:2px solid #999}
.author b{font-size:14px;display:block}
.author small{font-size:11px;color:#444}

/* tips */
.tips{left:0;top:2393px;width:1200px;height:630px;background:var(--soft)}
.tip{position:absolute;top:2573px;width:293px}
.tip .ph{height:222px}
.tip h3{font-family:"Montserrat",sans-serif;font-weight:600;font-size:17px;margin-top:25px}
.tip p{font-size:13px;line-height:19px;margin-top:12px;color:var(--muted);height:60px}
.tip .btn{position:relative;width:110px;height:33px;font-size:12px;margin-left:3px;margin-top:15px}

/* join */
.join{left:0;top:3023px;width:1200px;height:375px;background:linear-gradient(180deg,#1ea6ec,#148fdb);color:#fff;text-align:center}
.join h2{position:absolute;left:0;width:1200px;top:56px;font-family:"Montserrat",sans-serif;font-weight:600;font-size:40px}
.join p{position:absolute;left:0;width:1200px;top:120px;font-size:19px}
.field{position:absolute;top:176px;width:330px;height:49px;background:#fff;color:#444;font-size:13px;text-align:left;padding:16px 20px}

/* partners */
.inspired{left:0;top:3398px;width:1200px;height:279px;background:#fff}
.inspired h4{position:absolute;left:0;top:55px;width:1200px;text-align:center;font-weight:600;font-size:18px;line-height:29px}

/* cta */
.cta{left:0;top:3677px;width:1200px;height:298px;background:linear-gradient(180deg,#3f3f3f,#2f2f2f);color:#fff}
.cta h2{position:absolute;left:0;width:1200px;top:78px;text-align:center;font-family:"Montserrat",sans-serif;font-weight:600;font-size:31px}

/* footer */
.footer{left:0;top:3975px;width:1200px;height:332px;background:var(--footer);color:#ddd}
.col-title{position:absolute;top:50px;font-family:"Montserrat",sans-serif;font-weight:700;font-size:11.5px;color:#fff}
.fline{position:absolute;font-size:11px;line-height:18px;color:#ccc}
.social{position:absolute;display:flex;gap:12px;align-items:center;font-size:11px;color:#ccc}
.social i{width:22px;height:22px;border-radius:50%;display:block}
.copy{position:absolute;left:0;top:281px;width:1190px;text-align:center;font-size:10px;color:#bbb}
</style>
</head>
<body>

<header class="site-header">
  <div class="brand" style="left:132px;top:36px;font-size:33px;color:#444">Loftwise<span class="mark"></span></div>
  <div class="abs follow">FOLLOW US
    <span class="dot" style="background:#3b5998"></span><span class="dot" style="background:#1da1f2"></span><span class="dot" style="background:#0077b5"></span><span class="dot" style="background:#d33"></span><span class="dot" style="background:#333"></span>
  </div>
  <div class="btn" style="left:879px;top:21px;width:190px;height:39px;font-size:15px">SUBSCRIBE NOW</div>
  <nav class="abs nav"><span class="active">HOME</span><span>ABOUT</span><span>SHOP</span><span>BOOKS</span><span>BLOG</span><span>EXECUTIVE HEALTH</span><span>CONTACT</span></nav>
</header>

<section>
  <div class="abs hero" role="img" aria-label="Photo of a young professional looking at a tablet at night with city lights behind"></div>
  <div class="abs hero-glow"></div>
  <div class="abs hero-box">
    <h1>Loft Wise</h1>
    <p>Take Yourself Up to the Next Level.</p>
    <ul>
      <li><svg width="14" height="12" viewBox="0 0 14 12"><path d="M1 6l4 4 8-9" stroke="#fff" stroke-width="2.5" fill="none"/></svg>More Success</li>
      <li><svg width="14" height="12" viewBox="0 0 14 12"><path d="M1 6l4 4 8-9" stroke="#fff" stroke-width="2.5" fill="none"/></svg>Higher Productivity</li>
      <li><svg width="14" height="12" viewBox="0 0 14 12"><path d="M1 6l4 4 8-9" stroke="#fff" stroke-width="2.5" fill="none"/></svg>Better Health</li>
    </ul>
  </div>
  <div class="abs dots"><i></i><i class="on"></i><i></i><i></i></div>
</section>

<section>
  <div class="abs topics"></div>
  <h2 class="section-title" style="top:700px">This site provides you with<br>eye opening advice on</h2>
  <div class="abs grid">
    <div class="card"><svg width="60" height="56" viewBox="0 0 60 56"><path d="M30 30C18 20 14 12 20 6c4-4 8-2 10 2 2-4 6-6 10-2 6 6 2 14-10 24z" fill="#1aa3e6"/><path d="M4 38c10-2 18 4 26 4h16c6 0 10-4 12-6v10c-6 6-16 8-26 8H4z" fill="#1aa3e6"/></svg>HEALTH &amp;<br>PRODUCTIVITY</div>
    <div class="card"><svg width="60" height="56" viewBox="0 0 60 56"><circle cx="30" cy="12" r="7" fill="#1aa3e6"/><path d="M30 22v30M12 20l18 14 18-14" stroke="#1aa3e6" stroke-width="6" fill="none" stroke-linecap="round"/></svg>STRESS REDUCTION<br>&amp; SLEEP</div>
    <div class="card hl"><svg width="60" height="56" viewBox="0 0 60 56"><circle cx="30" cy="30" r="18" stroke="#fff" stroke-width="5" fill="none"/><path d="M30 30l14-14" stroke="#fff" stroke-width="5"/></svg>EXERCISE<span class="more">READ MORE</span></div>
    <div class="card"><svg width="70" height="60" viewBox="0 0 70 60"><circle cx="30" cy="30" r="24" fill="#1aa3e6"/><path d="M36 30l30-8-4 8-24 4z" fill="#1aa3e6" stroke="#fff" stroke-width="2"/></svg>TRAVELING</div>
    <div class="card"><svg width="70" height="56" viewBox="0 0 70 56"><rect x="6" y="10" width="14" height="20" rx="6" fill="#1aa3e6"/><rect x="50" y="10" width="14" height="20" rx="6" fill="#1aa3e6"/><rect x="16" y="18" width="38" height="12" fill="#1aa3e6"/><rect x="26" y="28" width="18" height="26" fill="#1aa3e6"/></svg>STRESS MANAGEMENT<br>COURSES</div>
    <div class="card"><svg width="60" height="56" viewBox="0 0 60 56"><circle cx="30" cy="14" r="9" fill="#1aa3e6"/><path d="M10 30h40M30 26v28" stroke="#1aa3e6" stroke-width="8" stroke-linecap="round"/></svg>FITNESS BOOT CAMPS<br>FOR EXECUTIVES</div>
    <div class="card"><svg width="64" height="56" viewBox="0 0 64 56"><circle cx="32" cy="10" r="8" fill="#1aa3e6"/><path d="M22 22h20v16H22z" fill="#1aa3e6"/><ellipse cx="32" cy="46" rx="28" ry="7" fill="#1aa3e6"/></svg>MINDFULNESS<br>COURSES</div>
    <div class="card"><svg width="60" height="56" viewBox="0 0 60 56"><path d="M30 10a20 20 0 1 0 20 28A16 16 0 0 1 30 10z" fill="#1aa3e6"/><circle cx="44" cy="10" r="4" fill="#1aa3e6"/><circle cx="52" cy="22" r="3" fill="#1aa3e6"/></svg>COURSES FOR<br>HEALTHY SLEEP</div>
    <div class="card"><svg width="60" height="56" viewBox="0 0 60 56"><rect x="4" y="14" width="52" height="38" rx="4" fill="#1aa3e6"/><rect x="22" y="6" width="16" height="10" rx="2" stroke="#1aa3e6" stroke-width="4" fill="none"/><path d="M18 14v38M42 14v38" stroke="#fff" stroke-width="3"/></svg>WORK-LIFE<br>BALANCE</div>
    <div class="card all"><svg width="26" height="24" viewBox="0 0 26 24"><path d="M3 3l9 9-9 9M13 3l9 9-9 9" stroke="#fff" stroke-width="3" fill="none"/></svg>VIEW ALL</div>
  </div>
</section>

<section>
  <div class="abs welcome-photo" role="img" aria-label="Photo of a businessman climbing wide steps toward a bright city skyline"></div>
  <div class="abs welcome">
    <div class="intro">Welcome to</div>
    <h2>LOFT WISE</h2>
    <p>To provide managers and executives with top in class health, fitness and diet advice so that they can reach the maximum productivity and energy level to be successful and happy in their business and private life.</p>
    <div class="btn" style="left:70px;top:366px;width:154px;height:46px;font-size:16px">READ MORE</div>
  </div>
</section>

<section>
  <div class="abs testimonials"></div>
  <h2 class="section-title" style="top:1865px;font-size:38px;line-height:46px">Testimonials</h2>
  <svg class="abs" style="left:178px;top:2097px" width="44" height="50" viewBox="0 0 44 50"><path d="M44 0v50L0 25z" fill="#555"/><path d="M28 19l-6 6 6 6" stroke="#fff" stroke-width="2" fill="none"/></svg>
  <svg class="abs" style="left:972px;top:2097px" width="44" height="50" viewBox="0 0 44 50"><path d="M0 0v50l44-25z" fill="#555"/><path d="M16 19l6 6-6 6" stroke="#fff" stroke-width="2" fill="none"/></svg>
  <div class="abs quote-box">
    <span class="qmark" style="left:118px;top:18px">“</span>
    <p>In the past I thought that my success only depends on working harder and harder. Loftwise.com made me aware that I need to work smarter and that my success depends not only on my brain but also on my body.</p>
    <span class="qmark" style="left:498px;top:138px">”</span>
    <div class="author"><span class="avatar"></span><div><b>Paolo Ventresca</b><small>VP Italy</small></div></div>
  </div>
</section>

<section>
  <div class="abs tips"></div>
  <h2 class="section-title" style="top:2443px">Read the latest tips on<br>healthy productivity</h2>
  <article class="tip" style="left:132px">
    <div class="ph" role="img" aria-label="Photo of business people silhouetted walking in a bright office" style="background:linear-gradient(180deg,#d9e6f2,#5a7394 55%,#1e2c40)"></div>
    <h3>HEALTHY SLEEP</h3>
    <p>Do you toss (and turn) for hours at night and perhaps can't sleep until the wee hours of the morning?</p>
    <div class="btn">READ MORE</div>
  </article>
  <article class="tip" style="left:453px">
    <div class="ph" role="img" aria-label="Photo of a cheering team of colleagues celebrating in an office" style="background:linear-gradient(180deg,#e7e7e7,#8a8a8a 55%,#2b2b2b)"></div>
    <h3>GENERAL HEALTH</h3>
    <p>Are you suffering from eye fatigue, blurred vision or headaches? You may experience computer vision syndrome.</p>
    <div class="btn">READ MORE</div>
  </article>
  <article class="tip" style="left:775px">
    <div class="ph" role="img" aria-label="Photo of a confident business team walking down a corridor" style="background:linear-gradient(180deg,#d2dde2,#7f8f96 50%,#3a3d44)"></div>
    <h3>FITNESS</h3>
    <p>Tossing and turning all night, ruminating about tomorrow's big presentation? Running your mind over...</p>
    <div class="btn">READ MORE</div>
  </article>
</section>

<section class="abs join">
  <h2>Join the movement</h2>
  <p>Get free, exclusive tips in your inbox to become a healthy manager.</p>
  <div class="field" style="left:264px">NAME</div>
  <div class="field" style="left:605px">E MAIL</div>
  <div class="btn" style="left:532px;top:262px;width:136px;height:48px;font-size:17px">SIGNUP</div>
</section>

<section class="abs inspired">
  <h4>THE WEBSITE CONTENT IS INSPIRED<br>BY THE RESEARCH AND PUBLICATIONS OF:</h4>
  <div class="abs" style="left:135px;top:168px;width:54px;height:64px;border-radius:6px;background:#c9ced8"></div>
  <div class="abs" style="left:292px;top:178px;width:126px;height:36px;border-radius:4px;background:#d9c4c6"></div>
  <div class="abs" style="left:522px;top:172px;width:150px;height:50px;background:#d8d8d8"></div>
  <div class="abs" style="left:790px;top:166px;width:60px;height:60px;background:#3b8fd0"></div>
  <div class="abs" style="left:950px;top:176px;width:40px;height:40px;border-radius:50%;background:#7a8fb8"></div>
</section>

<section class="abs cta" role="img" aria-label="Dark background photo of a businessman facing a city at dusk">
  <h2>Start your path to health &amp; success now!</h2>
  <div class="btn" style="left:489px;top:158px;width:222px;height:50px;font-size:17px">SUBSCRIBE NOW</div>
</section>

<footer class="abs footer">
  <div class="brand" style="left:152px;top:115px;font-size:30px;color:#fff">Loftwise<span class="mark"></span></div>
  <div class="col-title" style="left:523px">CONTACT US</div>
  <svg class="abs" style="left:523px;top:84px" width="10" height="13" viewBox="0 0 10 13"><path d="M5 13C1 8 0 6 0 5a5 5 0 0 1 10 0c0 1-1 3-5 8z" fill="#ccc"/><circle cx="5" cy="5" r="2" fill="#2a2a2a"/></svg>
  <div class="fline" style="left:544px;top:80px">2450 Birchwood Lane<br>Ashford, CA 90000</div>
  <svg class="abs" style="left:523px;top:131px" width="11" height="11" viewBox="0 0 11 11"><path d="M2 0l3 3-2 2c1 2 2 3 3 3l2-2 3 3-2 2C4 11 0 7 0 2z" fill="#ccc"/></svg>
  <div class="fline" style="left:544px;top:127px">555.010.2040</div>
  <svg class="abs" style="left:522px;top:166px" width="12" height="9" viewBox="0 0 12 9"><rect width="12" height="9" fill="#ccc"/><path d="M0 0l6 5 6-5" stroke="#2a2a2a" fill="none"/></svg>
  <div class="fline" style="left:544px;top:162px">info@loftwise.com</div>

  <div class="col-title" style="left:759px">MENU</div>
  <div class="fline" style="left:759px;top:82px;line-height:17.5px">HOME<br>ABOUT<br>SHOP<br>BOOKS<br>BLOG<br>EXECUTIVE HEALTH<br>CONTACT</div>

  <div class="col-title" style="left:946px">CONNECT WITH US</div>
  <div class="social" style="left:946px;top:84px"><i style="background:#1b6fd8"></i>Facenote</div>
  <div class="social" style="left:946px;top:123px"><i style="background:#1aa3e6"></i>Chirper</div>
  <div class="social" style="left:946px;top:162px"><i style="background:#1a1a1a;border:1px solid #444"></i>Linkpro</div>

  <div class="copy">Copyrights @ 2019 All Rights Reserved</div>
</footer>

</body>
</html>
```